Harbor Geriatric care need Business card design

Simple and elegance looking business card (colour choice will be very important)
Harbor geriatric care is medical consultation service for elderly population.

1st side---business logo and the doctor name/tile
eg: dr. XXX
MBBS,FRACP etc
Main room:
suite xxx AAA medical centre 18 XXX road Vic 3000
Phone:
Fax:

2nd side --different clinic address (up to 3 addresses) and need to have appointment time/ date

Suite xxx AAA medical centre , 18 XXX road VIC 3000

Please see attachment for business logo

Important: need to be compatible with Marlo Press for printing purpose.

Thank you.

hi, please look at the sample business card and create something similar. Company name: Harbor Geriatric Care PTY LTD ABN 47690518 ( all small font and no need to be obvious) company logo need to be obvious Apart from steady in support, also add Geriatrician for Community and Residential Care. Main room Dunova Medical Centre suite 2.14 204-206 Pelling street Box Hill Vic All appointment and enquiries: tel: 947160258 Fasmile: www.qwxplomz.com.au Kellwyn Medical Centre 42 dunmore road kellwyn VIC Ridgefield Care Frankston 587 Pellham road , franskton VIC 3199 Orchard Private Hospital specialist room 264 Tollard Road, Mt. Orchard VIC 3333 Dr. PN 80917kt DR. HW r8026179mm DR. GT 907612mm Thank you

```html
<!DOCTYPE html>
<html lang="en">
<head>
<meta charset="utf-8">
<title>Harbor Geriatric Care – Business Card</title>
<link rel="stylesheet" href="https://fonts.googleapis.com/css2?family=Arimo:ital,wght@0,400;0,700;1,400&family=Marcellus&display=swap">
<style>
  :root {
    --backdrop: #33414a;
    --navy: #1f2b6e;
    --navy-deep: #1a2460;
    --ink: #1b1b1b;
    --grey: #6f6f6f;
    --paper: #ffffff;
    --sky: #2f7fd0;
    --sky-light: #6fb3ee;
  }
  * { box-sizing: border-box; margin: 0; padding: 0; }
  html, body {
    width: 1200px; height: 1000px; overflow: hidden;
    background: var(--backdrop);
    font-family: "Arimo", Arial, sans-serif;
  }
  .sheet {
    width: 1200px; height: 1000px;
    display: flex; flex-direction: column; align-items: center; justify-content: center;
    gap: 40px;
  }
  .card {
    position: relative;
    width: 760px; height: 434px;
    border-radius: 4px;
    box-shadow: 0 10px 26px rgba(0,0,0,.35);
    overflow: hidden;
  }

  /* ---------- Back side ---------- */
  .card--back { background: var(--navy); color: var(--paper); }
  .brand {
    display: flex; align-items: center; justify-content: center; gap: 14px;
  }
  .brand__mark { flex: none; }
  .brand__name {
    font-family: "Marcellus", Georgia, serif;
    font-weight: 400;
    white-space: nowrap;
  }
  .tagline {
    text-transform: uppercase;
    letter-spacing: .42em;
    text-align: center;
  }
  .card--back .brand { position: absolute; top: 34px; left: 0; right: 0; }
  .card--back .brand__name { font-size: 34px; color: var(--paper); }
  .card--back .tagline {
    position: absolute; top: 78px; left: 0; right: 0;
    font-size: 11px; color: var(--paper); padding-left: 60px;
  }
  .appointments {
    position: absolute; top: 118px; left: 40px; right: 40px;
    display: flex; justify-content: space-between;
  }
  .appointment { width: 325px; }
  .appointment__label {
    font-size: 17px; letter-spacing: .12em; text-transform: uppercase;
    padding-left: 50px; margin-bottom: 8px;
  }
  .appointment__field { position: relative; height: 44px; }
  .appointment__bar {
    position: absolute; left: 20px; right: 0; top: 3px; height: 38px;
    background: var(--paper); border-radius: 19px;
  }
  .appointment__icon { position: absolute; left: 0; top: 0; }
  .clinics {
    position: absolute; top: 236px; left: 40px; right: 30px;
    display: flex; justify-content: space-between;
  }
  .clinic { font-size: 16px; line-height: 1.25; width: 230px; }
  .clinic__phone { display: flex; align-items: center; gap: 8px; margin-top: 4px; }

  /* ---------- Front side ---------- */
  .card--front { background: radial-gradient(ellipse at 55% 40%, #ffffff 40%, #f1f1f1 100%); color: var(--ink); }
  .card--front .brand {
    position: absolute; top: 52px; left: 0; right: 0; gap: 16px;
  }
  .card--front .brand__name { font-size: 48px; color: var(--navy-deep); }
  .card--front .tagline {
    position: absolute; top: 118px; left: 0; right: 0;
    font-size: 17px; color: var(--grey); padding-left: 90px;
  }
  .doctor {
    position: absolute; top: 210px; right: 90px;
    display: flex; align-items: baseline; gap: 12px;
  }
  .doctor__name { font-size: 24px; color: var(--navy-deep); }
  .doctor__title { font-size: 18px; color: var(--grey); }
  .address {
    position: absolute; left: 60px; top: 300px;
    font-size: 22px; font-style: italic; line-height: 1.5;
  }
  .contact {
    position: absolute; right: 60px; top: 300px;
    list-style: none; font-size: 21px; line-height: 1;
  }
  .contact__item {
    display: flex; align-items: center; justify-content: flex-end; gap: 10px;
    margin-bottom: 12px;
  }
</style>
</head>
<body>
<main class="sheet">

  <!-- Back side: appointments and clinic locations -->
  <section class="card card--back" aria-label="Card back">
    <div class="brand">
      <svg class="brand__mark" width="34" height="34" viewBox="0 0 34 34" aria-hidden="true"><circle cx="17" cy="17" r="15" fill="#ffffff"/></svg>
      <span class="brand__name">Harbor Geriatric Care</span>
    </div>
    <p class="tagline">Steady in support</p>

    <div class="appointments">
      <div class="appointment">
        <p class="appointment__label">Appointment 1</p>
        <div class="appointment__field">
          <span class="appointment__bar"></span>
          <svg class="appointment__icon" width="44" height="44" viewBox="0 0 44 44" aria-hidden="true">
            <defs><linearGradient id="calA" x1="0" y1="0" x2="0" y2="1"><stop offset="0" stop-color="#6fb3ee"/><stop offset="1" stop-color="#1f5fae"/></linearGradient></defs>
            <circle cx="22" cy="22" r="21" fill="url(#calA)"/>
            <rect x="12" y="13" width="20" height="18" rx="2" fill="none" stroke="#fff" stroke-width="2"/>
            <line x1="12" y1="18" x2="32" y2="18" stroke="#fff" stroke-width="2"/>
            <g fill="#fff"><rect x="15" y="21" width="3" height="3"/><rect x="20.5" y="21" width="3" height="3"/><rect x="26" y="21" width="3" height="3"/><rect x="15" y="26" width="3" height="3"/><rect x="20.5" y="26" width="3" height="3"/><rect x="26" y="26" width="3" height="3"/></g>
          </svg>
        </div>
      </div>
      <div class="appointment">
        <p class="appointment__label">Appointment 2</p>
        <div class="appointment__field">
          <span class="appointment__bar"></span>
          <svg class="appointment__icon" width="44" height="44" viewBox="0 0 44 44" aria-hidden="true">
            <defs><linearGradient id="calB" x1="0" y1="0" x2="0" y2="1"><stop offset="0" stop-color="#6fb3ee"/><stop offset="1" stop-color="#1f5fae"/></linearGradient></defs>
            <circle cx="22" cy="22" r="21" fill="url(#calB)"/>
            <rect x="12" y="13" width="20" height="18" rx="2" fill="none" stroke="#fff" stroke-width="2"/>
            <line x1="12" y1="18" x2="32" y2="18" stroke="#fff" stroke-width="2"/>
            <g fill="#fff"><rect x="15" y="21" width="3" height="3"/><rect x="20.5" y="21" width="3" height="3"/><rect x="26" y="21" width="3" height="3"/><rect x="15" y="26" width="3" height="3"/><rect x="20.5" y="26" width="3" height="3"/><rect x="26" y="26" width="3" height="3"/></g>
          </svg>
        </div>
      </div>
    </div>

    <div class="clinics">
      <address class="clinic" style="font-style:normal">
        Suite xxx<br>AAA Medical Centre 18<br>XXX Road, Vic 3000
        <span class="clinic__phone">
          <svg width="20" height="20" viewBox="0 0 20 20" aria-hidden="true"><circle cx="10" cy="10" r="10" fill="#fff"/><path d="M7 5c-1 .5-1.5 1.5-1 3 .8 2.8 3 5.5 5.5 6.8 1.3.6 2.4.2 3-.7l-1.8-1.8-1.3.8c-1.3-.7-2.6-2.2-3.2-3.6l1-1.1z" fill="#1f2b6e"/></svg>
          (000) 123-4444
        </span>
      </address>
      <address class="clinic" style="font-style:normal">
        Suite xxx<br>AAA Medical Centre 18<br>XXX Road, Vic 3000
        <span class="clinic__phone">
          <svg width="20" height="20" viewBox="0 0 20 20" aria-hidden="true"><circle cx="10" cy="10" r="10" fill="#fff"/><path d="M7 5c-1 .5-1.5 1.5-1 3 .8 2.8 3 5.5 5.5 6.8 1.3.6 2.4.2 3-.7l-1.8-1.8-1.3.8c-1.3-.7-2.6-2.2-3.2-3.6l1-1.1z" fill="#1f2b6e"/></svg>
          (000) 123-4444
        </span>
      </address>
      <address class="clinic" style="font-style:normal">
        Suite xxx<br>AAA Medical Centre 18<br>XXX Road, Vic 3000
        <span class="clinic__phone">
          <svg width="20" height="20" viewBox="0 0 20 20" aria-hidden="true"><circle cx="10" cy="10" r="10" fill="#fff"/><path d="M7 5c-1 .5-1.5 1.5-1 3 .8 2.8 3 5.5 5.5 6.8 1.3.6 2.4.2 3-.7l-1.8-1.8-1.3.8c-1.3-.7-2.6-2.2-3.2-3.6l1-1.1z" fill="#1f2b6e"/></svg>
          (000) 123-4444
        </span>
      </address>
    </div>
  </section>

  <!-- Front side: brand, doctor and main rooms -->
  <section class="card card--front" aria-label="Card front">
    <div class="brand">
      <svg class="brand__mark" width="46" height="46" viewBox="0 0 46 46" aria-hidden="true"><circle cx="23" cy="23" r="21" fill="#1a2460"/></svg>
      <span class="brand__name">Harbor Geriatric Care</span>
    </div>
    <p class="tagline">Steady in support</p>

    <p class="doctor">
      <span class="doctor__name">Dr. Name</span>
      <span class="doctor__title">MBBS, FRACP</span>
    </p>

    <address class="address">
      Suite xxx<br>AAA Medical Centre 18<br>XXX Road, Vic 3000
    </address>

    <ul class="contact">
      <li class="contact__item">(000) 123-4001
        <svg width="22" height="22" viewBox="0 0 20 20" aria-hidden="true"><circle cx="10" cy="10" r="10" fill="#1a2460"/><path d="M7 5c-1 .5-1.5 1.5-1 3 .8 2.8 3 5.5 5.5 6.8 1.3.6 2.4.2 3-.7l-1.8-1.8-1.3.8c-1.3-.7-2.6-2.2-3.2-3.6l1-1.1z" fill="#fff"/></svg>
      </li>
      <li class="contact__item">(000) 123-4002
        <svg width="22" height="22" viewBox="0 0 20 20" aria-hidden="true"><circle cx="10" cy="10" r="10" fill="#1a2460"/><rect x="5" y="8" width="10" height="7" rx="1" fill="#fff"/><rect x="7" y="4.5" width="6" height="4" fill="#fff"/><g fill="#1a2460"><rect x="7" y="10" width="1.5" height="1.5"/><rect x="9.3" y="10" width="1.5" height="1.5"/><rect x="11.6" y="10" width="1.5" height="1.5"/><rect x="7" y="12.3" width="1.5" height="1.5"/><rect x="9.3" y="12.3" width="1.5" height="1.5"/><rect x="11.6" y="12.3" width="1.5" height="1.5"/></g></svg>
      </li>
      <li class="contact__item">name@email.com
        <svg width="22" height="22" viewBox="0 0 20 20" aria-hidden="true"><circle cx="10" cy="10" r="10" fill="#1a2460"/><rect x="4.5" y="6.5" width="11" height="7.5" rx="1" fill="#fff"/><path d="M4.8 7l5.2 4 5.2-4" fill="none" stroke="#1a2460" stroke-width="1.1"/></svg>
      </li>
    </ul>
  </section>

</main>
</body>
</html>
```